Vibrant, yet professional, stationery set and other designs required.

I need to source a fantastic designer for a new project as part of my company using a new logo designed via pixel harbor.

**UPDATE** I am not looking for just 'fine' design that will suffice. I am looking for something great.

We are a life assurance brokerage based in Dublin, Ireland and HearthGuard.ie is our new website aimed at providing services for young families in Ireland. We are hoping to be the 'Vorn' level of service providers in this area and I am looking for the quality of design to reflect this :-) Hopefully that makes sense!

I have a preference for straight lines over curves and waves.

I need...

1. Business card
2. Letterhead
3. Banner (for printing - 76cm X 305cm)
4. Car branding for ZELKA 300 (2014 sport model) I believe the templates are freely available online.

Target Market(s)

Parents in Ireland - Aged 27 to 50.

Industry/Entity Type

Financial Planning

Colors

Designer to choose colors to be used in the design.

Requirements
Must have
• All of the items listed in the description above. I like clean, bright, legible, vibrant and professional design.
Should not have
• No silly or 'cheap' looking designs. This is a professional company looking to provide a professional service.

```html
<!DOCTYPE html>
<html lang="en">
<head>
<meta charset="utf-8">
<title>HearthGuard.ie – Business Card</title>
<link href="https://fonts.googleapis.com/css2?family=Roboto:wght@400;500&display=swap" rel="stylesheet">
<style>
  :root {
    --backdrop: #b3b3b3;
    --orange: #f0821a;
    --white: #ffffff;
    --card-white: #f7f7f7;
    --slate: #8a969b;
    --slate-dark: #5d676b;
    --text: #4a4a4a;
    --sky: #6cc4e0;
    --lime: #9bc43c;
  }
  html, body {
    margin: 0;
    padding: 0;
    width: 1200px;
    height: 960px;
    overflow: hidden;
    background: var(--backdrop);
    font-family: 'Roboto', Arial, sans-serif;
  }
  .canvas {
    position: relative;
    width: 1200px;
    height: 960px;
  }
  .card {
    position: absolute;
    box-sizing: border-box;
  }
  .card-front {
    left: 320px;
    top: 105px;
    width: 610px;
    height: 340px;
    background: var(--orange);
    display: flex;
    align-items: center;
    justify-content: center;
  }
  .brand-name {
    font-weight: 500;
    letter-spacing: -0.5px;
    white-space: nowrap;
  }
  .card-front .brand-name {
    color: var(--white);
    font-size: 62px;
  }
  .card-back {
    left: 320px;
    top: 493px;
    width: 600px;
    height: 344px;
    background: var(--card-white);
  }
  .card-back .brand-name {
    position: absolute;
    right: 34px;
    top: 52px;
    color: var(--slate);
    font-size: 42px;
  }
  .contact {
    position: absolute;
    left: 27px;
    top: 133px;
    color: var(--text);
  }
  .person-name {
    margin: 0;
    color: var(--orange);
    font-weight: 500;
    font-size: 18px;
    line-height: 22px;
  }
  .person-role {
    margin: 2px 0 10px;
    color: var(--slate);
    font-size: 14px;
    line-height: 18px;
  }
  .address {
    margin: 0 0 4px;
    font-size: 14px;
    line-height: 19px;
    font-style: normal;
  }
  .contact-list {
    list-style: none;
    margin: 0;
    padding: 0;
    font-size: 14px;
  }
  .contact-list li {
    display: flex;
    align-items: center;
    height: 19px;
  }
  .contact-list svg {
    width: 13px;
    height: 13px;
    margin-right: 10px;
    fill: var(--orange);
  }
  .footer-band {
    position: absolute;
    left: 0;
    bottom: 0;
    width: 600px;
    height: 34px;
  }
  .website {
    position: absolute;
    left: 28px;
    bottom: 8px;
    color: var(--white);
    font-size: 13px;
    letter-spacing: 3.4px;
  }
</style>
</head>
<body>
<main class="canvas">

  <section class="card card-front">
    <span class="brand-name">HearthGuard.ie</span>
  </section>

  <section class="card card-back">
    <span class="brand-name">HearthGuard.ie</span>

    <div class="contact">
      <h1 class="person-name">AIDAN BRENNAN</h1>
      <p class="person-role">CEO/FOUNDER</p>
      <address class="address">42 Larch Row<br>Ranelagh, Dublin D06 K2P4</address>
      <ul class="contact-list">
        <li>
          <svg viewBox="0 0 16 16" aria-hidden="true"><path d="M3.5 1l3 3-1.8 2.2c.9 1.9 2.3 3.3 4.2 4.2L11 8.6l3 3-2 2.4C6.5 13.5 2.5 9.5 1 4z"/></svg>
          601 284 7730
        </li>
        <li>
          <svg viewBox="0 0 16 16" aria-hidden="true"><path d="M4 0h8a1 1 0 0 1 1 1v14a1 1 0 0 1-1 1H4a1 1 0 0 1-1-1V1a1 1 0 0 1 1-1zm1 2v10h6V2zm3 11a1 1 0 1 0 0 2 1 1 0 0 0 0-2z"/></svg>
          087 512 3946
        </li>
        <li>
          <svg viewBox="0 0 16 16" aria-hidden="true"><path d="M4 1h8v4H4zM1 6h14v7h-3v-3H4v3H1zm4 5h6v4H5z"/></svg>
          601 284 7731
        </li>
        <li>
          <svg viewBox="0 0 16 16" aria-hidden="true"><path d="M1 3h14v1.5L8 9 1 4.5zm0 3.2l7 4.5 7-4.5V13H1z"/></svg>
          aidan@hearthguard.ie
        </li>
      </ul>
    </div>

    <svg class="footer-band" viewBox="0 0 600 34" aria-hidden="true">
      <polygon points="0,0 254,0 278,24 600,24 600,34 0,34" fill="var(--slate)"/>
      <polygon points="270,10 380,10 394,24 284,24" fill="var(--sky)"/>
      <polygon points="384,10 506,10 520,24 398,24" fill="var(--orange)"/>
      <polygon points="510,10 600,10 600,24 524,24" fill="var(--lime)"/>
    </svg>
    <span class="website">www.hearthguard.ie</span>
  </section>

</main>
</body>
</html>
```